Ardenwell Building and Property Services needs a business card design

We need a business card design for our building and property services business. We already have a logo we just need a creative design and layout on a business card. Emphasis on clean, modern, professional.
Our client targets are mainly body corporates, building managers, construction managers.
We are a building services company that lean more to structural repair of buildings, through concrete rectification and carbon fibre strengthening.
We also refurbish facades, rendering, painting etc
We target higher end body corporates in prestigious locations, hence why we'd like our cards to reflect professionalism, strength, efficiency

Target Market(s)

body corporates, building managers, construction managers

Industry/Entity Type

Construction

Contact Information for Business Card

Ardenwell is the main word, with 'Building and Property Services' underneath.
Level 17, 82 Harlow Street
MERRIDALE
Melbourne
Vic 3094
T: 9518 2736
Duncan Ferris - Director
dunardenwell@mailbox-example.com

Requirements
Must have
• Stand out on the back of the card- strong/ bold, company logo
• All of the contact details written above
Should not have
• I'd like the card to stand out, especially on the back. Id like the company logo to be prominent, although feel free to be creative around it. But remain clean and professional

```html
<!DOCTYPE html>
<html lang="en">
<head>
<meta charset="utf-8">
<title>Ardenwell Building and Property Services – Business Card</title>
<link rel="stylesheet" href="https://fonts.googleapis.com/css2?family=Arimo:wght@400&display=swap">
<style>
  :root {
    --backdrop: #27292c;
    --brand-blue: #1f8fd0;
    --frame-light: #8fd4f5;
    --frame-deep: #2a5fc0;
    --silver-light: #f4f4f4;
    --silver-mid: #c9c9c9;
    --silver-edge: #8a8a8a;
    --label-grey: #a3a3a3;
    --ink: #111111;
    --rule-grey: #cfcfcf;
    --card-white: #ffffff;
  }
  * { margin: 0; padding: 0; box-sizing: border-box; }
  html, body { width: 1200px; height: 1000px; overflow: hidden; }
  body {
    position: relative;
    background: var(--backdrop);
    font-family: "Arimo", Arial, sans-serif;
  }
  .card {
    position: absolute;
    left: 406px;
    width: 388px;
    box-shadow: 4px 6px 10px rgba(0, 0, 0, 0.55);
  }
  .card-front {
    top: 205px;
    height: 232px;
    background: linear-gradient(180deg, var(--silver-light) 0%, #e2e2e2 25%, var(--silver-mid) 48%, var(--silver-light) 75%, #d6d6d6 100%);
    border: 3px solid var(--silver-edge);
  }
  .card-back {
    top: 562px;
    height: 234px;
    background: var(--card-white);
  }
  .frame {
    position: absolute;
    inset: 4px;
    border: 4px solid var(--frame-light);
    border-bottom-color: var(--frame-deep);
  }
  .card-back .frame { inset: 5px; }

  .brand-square {
    display: block;
    background: var(--brand-blue);
  }
  .brand-name,
  .brand-tagline {
    font-family: "Arimo", Arial, sans-serif;
    font-weight: 400;
    color: var(--brand-blue);
    text-transform: uppercase;
    line-height: 1;
  }

  .front-brand {
    position: absolute;
    left: 0; right: 0;
    top: 48px;
    text-align: center;
  }
  .front-brand .brand-square { width: 46px; height: 46px; margin: 0 auto 46px; }
  .front-brand .brand-name { font-size: 25px; letter-spacing: 2px; }
  .front-brand .brand-tagline { font-size: 6.5px; letter-spacing: 0.9px; margin-top: 4px; }

  .back-brand {
    position: absolute;
    top: 16px;
    left: 62px;
    display: flex;
    align-items: center;
    gap: 10px;
  }
  .back-brand .brand-square { width: 30px; height: 30px; }
  .back-brand .brand-name { font-size: 26px; letter-spacing: 2px; }
  .back-brand .brand-tagline { font-size: 8px; letter-spacing: 1px; margin-top: 3px; }
  .brand-rule {
    position: absolute;
    top: 60px;
    left: 67px;
    width: 254px;
    height: 1px;
    background: var(--rule-grey);
  }

  .person {
    position: absolute;
    right: 17px;
    top: 77px;
    text-align: right;
    line-height: 1;
  }
  .person-role { font-size: 14px; color: var(--label-grey); }
  .person-name { font-size: 15px; color: var(--ink); margin-top: 1px; }

  .details { position: absolute; top: 140px; font-size: 11.5px; line-height: 15px; color: var(--ink); }
  .details-label { color: var(--label-grey); }
  .details-address { left: 24px; }
  .details-contact { left: 186px; }
  .details-contact .email-label { margin-top: 16px; }
  .details-contact .email { font-size: 10.6px; }
  .details-divider {
    position: absolute;
    left: 171px;
    top: 140px;
    width: 1px;
    height: 66px;
    background: var(--label-grey);
  }
</style>
</head>
<body>
  <section class="card card-front" aria-label="Card front">
    <div class="frame"></div>
    <div class="front-brand">
      <span class="brand-square"></span>
      <div class="brand-name">Ardenwell</div>
      <div class="brand-tagline">Building and Property Services</div>
    </div>
  </section>

  <section class="card card-back" aria-label="Card back">
    <div class="frame"></div>
    <div class="back-brand">
      <span class="brand-square"></span>
      <div>
        <div class="brand-name">Ardenwell</div>
        <div class="brand-tagline">Building and Property Services</div>
      </div>
    </div>
    <div class="brand-rule"></div>

    <div class="person">
      <div class="person-role">Director</div>
      <div class="person-name">Duncan Ferris</div>
    </div>

    <div class="details details-address">
      <div class="details-label">Address :</div>
      <div>Level 17, 82 Harlow Street</div>
      <div>MERRIDALE</div>
      <div>Melbourne</div>
      <div>Vic 3094</div>
    </div>
    <div class="details-divider"></div>
    <div class="details details-contact">
      <div class="details-label">Contact :</div>
      <div>9518 2736</div>
      <div class="details-label email-label">E-mail :</div>
      <div class="email">dunardenwell@mailbox-example.com</div>
    </div>
  </section>
</body>
</html>
```